Marlow Naturopathics business card design

Using the marlow logo designed, we would like that incorporated into a business card. A colour scheme which works with the logo and lists the following business details:

Dennis Marlow - Naturopath
Level 1, 58 Torvane Street
Wollongong NSW
(02) 4391 7084
www.dennismarlowhealth-example.com

We would also like space on the back of the card for next appointment times.

Target Market(s)

Anyone looking to improve their health

Industry/Entity Type

Business

Requirements
Must have
• Marlow Naturopathics logo, business details.
Nice to have
• Good colour schemes, attractive, eye-catching features that are easy to read.

```html
<!DOCTYPE html>
<html lang="en">
<head>
<meta charset="utf-8">
<title>Marlow Naturopathics – Business Card</title>
<link rel="stylesheet" href="https://fonts.googleapis.com/css2?family=Jura:wght@500;600&display=swap">
<style>
  :root {
    --page-bg: #d6d5d3;
    --card-bg: #5f5954;
    --card-ink: #34302d;
    --card-edge: #4f4a46;
  }
  * { margin: 0; padding: 0; box-sizing: border-box; }
  html, body {
    width: 1200px;
    height: 900px;
    overflow: hidden;
    background: var(--page-bg);
  }
  .sheet {
    width: 1200px;
    height: 900px;
    display: flex;
    flex-direction: column;
    align-items: center;
    justify-content: center;
    gap: 30px;
  }
  .card {
    position: relative;
    width: 720px;
    height: 411px;
    background: var(--card-bg);
    border: 1px solid var(--card-edge);
    font-family: "Jura", sans-serif;
    color: var(--card-ink);
  }
  /* Details side */
  .card-back .brand-mini {
    position: absolute;
    top: 30px;
    left: 36px;
    display: flex;
    align-items: center;
    gap: 8px;
    font-size: 13px;
    font-weight: 600;
    letter-spacing: 0.5px;
  }
  .brand-mini .brand-dot {
    width: 12px;
    height: 12px;
    border-radius: 50%;
    background: var(--card-ink);
  }
  .card-back .person {
    position: absolute;
    top: 62px;
    left: 420px;
  }
  .person .person-name {
    font-size: 34px;
    font-weight: 600;
    letter-spacing: 1px;
    line-height: 1.1;
  }
  .person .person-role {
    font-size: 24px;
    font-weight: 600;
    letter-spacing: 1px;
    margin-top: 2px;
  }
  .card-back .contact {
    position: absolute;
    top: 222px;
    left: 340px;
    list-style: none;
    font-size: 19px;
    font-weight: 600;
    letter-spacing: 0.8px;
    line-height: 1.3;
  }
  /* Logo side */
  .card-front {
    display: flex;
    flex-direction: column;
    align-items: center;
    justify-content: center;
    gap: 18px;
  }
  .card-front .brand-circle {
    width: 90px;
    height: 90px;
    border-radius: 50%;
    background: var(--card-ink);
  }
  .card-front .brand-name {
    font-size: 34px;
    font-weight: 600;
    letter-spacing: 3px;
  }
</style>
</head>
<body>
  <main class="sheet">
    <section class="card card-back" aria-label="Card details side">
      <div class="brand-mini">
        <span class="brand-dot"></span>
        <span class="brand-mini-name">Marlow Naturopathics</span>
      </div>
      <div class="person">
        <p class="person-name">Dennis Marlow</p>
        <p class="person-role">Naturopath</p>
      </div>
      <ul class="contact">
        <li>Level 1, 58 Torvane Street</li>
        <li>Wollongong NSW</li>
        <li>(02) 4391 7084</li>
        <li>www.dennismarlowhealth-example.com</li>
      </ul>
    </section>

    <section class="card card-front" aria-label="Card brand side">
      <span class="brand-circle"></span>
      <p class="brand-name">Marlow Naturopathics</p>
    </section>
  </main>
</body>
</html>
```